BBQ Grill Tongs Logo and Packaging Design

Need fun exciting logo design and packaging for the best BBQ and Grilling tongs ever used.
Company Name is
Plunko's Tongs
www.flamepincher.example
Template layout for packaging is flat 5 x 8
We want the packaging to jump off the shelf in an eye catching design that uses vibrant colors and terminology such as..
NO more sore hands
Never Slips
Lifetime Guarantee
Best for Indoor and Outdoor BBQ and Cooking
Used by the BEST BBQ Grillmasters and Cooks
Target Market(s)
outdoor and indoor cooks, all ages people who purchase bbq supplies, cooking supplies and or bbq and grilling enthusists
Industry/Entity Type
Cooking
Requirements
Must have
- Bold Branding, bright colors
Nice to have
- http://www.renlomarsk.example/
- http://www.delvatuno.example/
- http://www.humblekettleworks.example/

```html
<!DOCTYPE html>
<html lang="en">
<head>
<meta charset="utf-8">
<title>Plunko's Tongs – Packaging</title>
<link href="https://fonts.googleapis.com/css2?family=Oswald:wght@400;600&display=swap" rel="stylesheet">
<style>
  :root {
    --bg: #e9e9e9;
    --red-bright: #d8141f;
    --red-deep: #8e0c12;
    --black: #0b0b0b;
    --white: #ffffff;
    --rule: #e0121c;
    --steel-light: #e4e8ee;
    --steel-dark: #9aa2ad;
    --flame-yellow: #ffc93a;
    --flame-orange: #f26a12;
    --flame-red: #b3160c;
  }
  * { box-sizing: border-box; margin: 0; padding: 0; }
  html, body { width: 1200px; height: 960px; overflow: hidden; }
  body {
    background: var(--bg);
    font-family: "Oswald", sans-serif;
    position: relative;
  }
  .dieline {
    position: absolute;
    left: 270px;
    top: 80px;
    display: flex;
    box-shadow: 0 20px 40px rgba(0,0,0,.25);
  }
  .panel {
    position: relative;
    height: 800px;
    overflow: hidden;
    background: linear-gradient(180deg, var(--red-bright) 0%, var(--red-deep) 30%, var(--black) 62%, var(--black) 100%);
    color: var(--white);
  }
  .panel--side { width: 160px; border-right: 1px solid rgba(0,0,0,.5); }
  .panel--front { width: 500px; }

  .brand-name {
    font-weight: 600;
    color: var(--white);
    text-transform: uppercase;
    line-height: .95;
    text-align: center;
  }
  .panel--front .brand-name { font-size: 74px; margin-top: 60px; letter-spacing: 1px; }
  .panel--side .brand-name { font-size: 30px; margin-top: 40px; }

  .claims { list-style: none; }
  .claims li {
    font-weight: 400;
    line-height: 1.15;
    border-bottom: 3px solid var(--rule);
  }
  .panel--front .claims {
    position: absolute; left: 40px; top: 300px; width: 230px;
  }
  .panel--front .claims li { font-size: 21px; padding-bottom: 8px; margin-bottom: 18px; }
  .panel--side .claims { margin: 40px 16px 0; }
  .panel--side .claims li { font-size: 11px; padding-bottom: 4px; margin-bottom: 10px; border-bottom-width: 2px; }

  .product-shot {
    position: absolute;
    background: linear-gradient(90deg, var(--steel-dark), var(--steel-light) 50%, var(--steel-dark));
    border-radius: 30px 30px 10px 10px;
    opacity: .9;
  }
  .panel--front .product-shot { left: 300px; top: 270px; width: 150px; height: 470px; transform: rotate(8deg); }
  .panel--side .product-shot { left: 30px; top: 420px; width: 70px; height: 330px; transform: rotate(-4deg); }

  .flames {
    position: absolute;
    left: 0; right: 0; bottom: 0;
    height: 190px;
    background: linear-gradient(180deg, rgba(179,22,12,0) 0%, var(--flame-red) 25%, var(--flame-orange) 60%, var(--flame-yellow) 100%);
  }
  .panel--side .flames { height: 170px; }
</style>
</head>
<body>
  <div class="dieline">
    <section class="panel panel--side">
      <h2 class="brand-name">Plunko's<br>Tongs</h2>
      <ul class="claims">
        <li>NO more sore hands</li>
        <li>Never Slips</li>
        <li>Lifetime Guarantee</li>
        <li>Best for Indoor and Outdoor BBQ and Cooking</li>
        <li>Used by the BEST BBQ Grillmasters and Cooks</li>
      </ul>
      <div class="product-shot" role="img" aria-label="Photo of stainless steel grill tongs with wooden grip"></div>
      <div class="flames" role="img" aria-label="Illustration of fire flames"></div>
    </section>
    <section class="panel panel--front">
      <h1 class="brand-name">Plunko's<br>Tongs</h1>
      <ul class="claims">
        <li>NO more sore hands</li>
        <li>Never Slips</li>
        <li>Lifetime Guarantee</li>
        <li>Best for Indoor and Outdoor BBQ and Cooking</li>
        <li>Used by the BEST BBQ Grillmasters and Cooks</li>
      </ul>
      <div class="product-shot" role="img" aria-label="Photo of stainless steel grill tongs with wooden grip"></div>
      <div class="flames" role="img" aria-label="Illustration of fire flames"></div>
    </section>
  </div>
</body>
</html>
```